Process Roadmap for Interior Design Firm

We are looking to ramp up the design appeal of our current process roadmap to be very visually interesting, while staying informative and descriptive about our process.

Target Market(s)

In-house Clients

Industry/Entity Type

Interior Design Firm focused on sustainable and holistic design.

Other font styles liked:
• raleway

Requirements
Must have
• 1.) it would be nice if the graphic provided a more clear indication of the “journey” from one step to the next, so that there was a clear sense of the progression (such that we are directing the viewer) 2.). We would want it to fit on an 8.5”x11” page (the page could be horizontal when we have the Steady Pathway formatted out with the testimonials) (in addition to the testimonials, we may also want to have the detailed descriptions of each step of the process presented below the graphic, so that the graphic is cleaner) 3.) ideally the graphic is clear and simple enough to also be used on our Bi-Weekly Client Updates, which will be typed updates for clients re their project budgets, schedule and scope. The Steady Pathway graphic (without all the testimonials) would be at the end of the update, and would fit on the page horizontally at the bottom, perhaps in a space which is 7.5”w x 4”h or so.
Should not have
• bold or bright colors. Natural neutrals are preferred, such as the ones featured on the provided graphic.

```html
<!DOCTYPE html>
<html lang="en">
<head>
<meta charset="utf-8">
<title>EHD Steady Pathway</title>
<link href="https://fonts.googleapis.com/css2?family=Montserrat:wght@600;700&family=Raleway:wght@400;500&display=swap" rel="stylesheet">
<style>
  :root {
    --gold: #b58f41;
    --gold-soft: #c9aa6e;
    --gold-line: #c3a263;
    --ink: #1f1f1f;
    --paper: #ffffff;
    --blush: #f5efe5;
    --icon: #ffffff;
  }
  * { margin: 0; padding: 0; box-sizing: border-box; }
  html, body { width: 1200px; height: 943px; overflow: hidden; background: var(--paper); }
  .sheet { position: relative; width: 1200px; height: 943px; background: var(--paper); font-family: "Raleway", sans-serif; color: var(--ink); }

  .brand { position: absolute; left: 60px; top: 80px; font-family: "Raleway", sans-serif; font-weight: 500; font-size: 17px; color: var(--gold); line-height: 1; white-space: nowrap; }

  .title { position: absolute; left: 280px; top: 64px; font-family: "Montserrat", sans-serif; font-weight: 700; font-size: 50px; letter-spacing: -0.5px; color: var(--gold); line-height: 1; }
  .site { position: absolute; right: 24px; top: 50px; font-size: 16px; letter-spacing: 2.6px; color: var(--gold); font-weight: 400; }
  .title-bar { position: absolute; left: 856px; top: 87px; width: 344px; height: 31px; }

  .diagram { position: absolute; left: 0; top: 0; }

  .step-name { position: absolute; top: 176px; width: 146px; text-align: center; font-family: "Montserrat", sans-serif; font-weight: 600; font-size: 19px; color: var(--gold-soft); }

  .step-note { position: absolute; font-size: 11.3px; line-height: 14.5px; font-weight: 500; color: var(--ink); }

  .testimonials-title { position: absolute; left: 0; width: 1200px; top: 712px; text-align: center; font-family: "Montserrat", sans-serif; font-weight: 700; font-size: 33px; color: var(--gold); }
  .quote { position: absolute; top: 776px; width: 175px; font-size: 14px; line-height: 18.2px; font-weight: 400; color: var(--ink); }
  .quote-num { position: absolute; top: 791px; width: 46px; height: 46px; border-radius: 50%; background: radial-gradient(circle at 40% 35%, #d6bb84, #b89452); box-shadow: 0 0 0 3px #efe3cc; color: #fff; font-family: "Montserrat", sans-serif; font-weight: 700; font-style: italic; font-size: 20px; line-height: 46px; text-align: center; }
</style>
</head>
<body>
<div class="sheet">

  <div class="brand">Elm Harbor Design</div>

  <h1 class="title">EHD Steady Pathway</h1>
  <div class="site">www.elmharbordesign.com</div>
  <svg class="title-bar" viewBox="0 0 344 31" aria-hidden="true">
    <g fill="#b58f41">
      <rect x="0" y="0" width="3" height="31"/>
      <rect x="7" y="0" width="3" height="31"/>
      <rect x="14" y="0" width="3" height="31"/>
      <rect x="21" y="0" width="3" height="31"/>
      <rect x="28" y="0" width="3" height="31"/>
      <rect x="35" y="0" width="3" height="31"/>
      <rect x="41" y="0" width="5" height="31"/>
      <rect x="50" y="0" width="294" height="31"/>
    </g>
  </svg>

  <svg class="diagram" width="1200" height="943" viewBox="0 0 1200 943">
    <defs>
      <radialGradient id="medal" cx="45%" cy="40%" r="65%">
        <stop offset="0" stop-color="#d1b47a"/>
        <stop offset="0.8" stop-color="#c6a669"/>
        <stop offset="1" stop-color="#b08d4d"/>
      </radialGradient>
      <polygon id="star" points="0,-8 2.4,-2.5 7.6,-2.5 3.5,1.2 4.9,6.5 0,3.4 -4.9,6.5 -3.5,1.2 -7.6,-2.5 -2.4,-2.5"/>
    </defs>

    <!-- pathway line -->
    <path fill="none" stroke="var(--gold-line)" stroke-width="1.4"
      d="M51 314 H91 V601 A73.5 73.5 0 0 0 238 601 V295 A73 73 0 0 1 384 295 V601 A73 73 0 0 0 530 601 V295 A73 73 0 0 1 676 295 V601 A73 73 0 0 0 822 601 V295 A73 73 0 0 1 968 295 V601 A73 73 0 0 0 1114 601 V314 H1151"/>
    <circle cx="43" cy="314" r="7.5" fill="#fff" stroke="var(--gold-line)" stroke-width="1.4"/>
    <circle cx="1159" cy="314" r="7.5" fill="#fff" stroke="var(--gold-line)" stroke-width="1.4"/>

    <g fill="#fff">
      <rect x="299" y="214" width="24" height="16"/>
      <rect x="591" y="214" width="24" height="16"/>
      <rect x="883" y="214" width="24" height="16"/>
    </g>

    <g fill="none" stroke="var(--gold)" stroke-width="1.3" stroke-linecap="round">
      <path d="M165 217 V229 M161 225 L165 229 L169 225"/>
      <path d="M311 217 V229 M307 225 L311 229 L315 225"/>
      <path d="M457 217 V229 M453 225 L457 229 L461 225"/>
      <path d="M603 217 V229 M599 225 L603 229 L607 225"/>
      <path d="M749 217 V229 M745 225 L749 229 L753 225"/>
      <path d="M895 217 V229 M891 225 L895 229 L899 225"/>
      <path d="M1041 217 V229 M1037 225 L1041 229 L1045 225"/>
    </g>

    <!-- step medallions -->
    <g fill="url(#medal)">
      <circle cx="165" cy="295" r="63"/><path d="M155 354 L165 366 L175 354 Z"/>
      <circle cx="311" cy="295" r="63"/><path d="M301 354 L311 366 L321 354 Z"/>
      <circle cx="457" cy="295" r="63"/><path d="M447 354 L457 366 L467 354 Z"/>
      <circle cx="603" cy="295" r="63"/><path d="M593 354 L603 366 L613 354 Z"/>
      <circle cx="749" cy="295" r="63"/><path d="M739 354 L749 366 L759 354 Z"/>
      <circle cx="895" cy="295" r="63"/><path d="M885 354 L895 366 L905 354 Z"/>
      <circle cx="1041" cy="295" r="63"/><path d="M1031 354 L1041 366 L1051 354 Z"/>
    </g>

    <!-- step icons -->
    <g fill="none" stroke="var(--icon)" stroke-width="2" stroke-linecap="round" stroke-linejoin="round">
      <g class="icon-listen" transform="translate(165 295)" role="img" aria-label="Listening icon: speech bubble">
        <path d="M-24 -18 H20 A6 6 0 0 1 26 -12 V10 A6 6 0 0 1 20 16 H-6 L-16 26 V16 H-24 A6 6 0 0 1 -30 10 V-12 A6 6 0 0 1 -24 -18 Z"/>
        <circle cx="-12" cy="-1" r="2" fill="var(--icon)"/><circle cx="-2" cy="-1" r="2" fill="var(--icon)"/><circle cx="8" cy="-1" r="2" fill="var(--icon)"/>
      </g>
      <g class="icon-vision" transform="translate(311 295)" role="img" aria-label="Visioning icon: house with an eye">
        <path d="M-28 -6 L0 -30 L28 -6 M-20 -12 V24 H20 V-12"/>
        <path d="M-16 8 Q0 -8 16 8 Q0 24 -16 8 Z"/>
        <circle cx="0" cy="8" r="5"/>
      </g>
      <g class="icon-plan" transform="translate(457 295)" role="img" aria-label="Planning icon: checklist">
        <rect x="-22" y="-28" width="44" height="58" rx="3"/>
        <rect x="-10" y="-32" width="20" height="8" rx="2"/>
        <path d="M-14 -10 L-11 -7 L-6 -13 M-14 4 L-11 7 L-6 1 M-14 18 L-11 21 L-6 15"/>
        <path d="M0 -10 H14 M0 4 H14 M0 18 H14"/>
      </g>
      <g class="icon-design" transform="translate(603 295)" role="img" aria-label="Designing icon: pencil and set square">
        <path d="M-26 28 V-8 L10 28 Z M-18 20 V12 L-10 20 Z"/>
        <path d="M6 -32 H16 V12 L11 20 L6 12 Z M6 -24 H16"/>
        <path d="M-2 30 H30"/>
      </g>
      <g class="icon-manage" transform="translate(749 295)" role="img" aria-label="Managing icon: budget and progress">
        <circle cx="-12" cy="-8" r="16"/>
        <path d="M-8 -16 Q-12 -19 -16 -16 Q-19 -12 -12 -8 Q-5 -4 -8 0 Q-12 3 -16 0 M-12 -22 V-19 M-12 3 V6"/>
        <path d="M6 28 V18 M16 28 V10 M26 28 V2 M2 30 H30"/>
      </g>
      <g class="icon-install" transform="translate(895 295)" role="img" aria-label="Installing icon: gear">
        <circle cx="0" cy="0" r="17" stroke-width="7" stroke-dasharray="5.3 8"/>
        <circle cx="0" cy="0" r="13"/>
        <circle cx="0" cy="0" r="6"/>
        <path d="M-28 -14 A31 31 0 0 1 14 -28 M28 14 A31 31 0 0 1 -14 28"/>
        <path d="M8 -32 L14 -28 L9 -22 M-8 32 L-14 28 L-9 22"/>
      </g>
      <g class="icon-complete" transform="translate(1041 295)" role="img" aria-label="Completing icon: stars">
        <use href="#star" x="-18" y="-10"/>
        <use href="#star" x="4" y="-22"/>
        <use href="#star" x="20" y="0"/>
        <use href="#star" x="0" y="8" transform="scale(0.9)"/>
        <path d="M-4 30 Q-10 10 -16 -1 M-2 30 Q2 10 4 -13 M0 30 Q10 16 18 8"/>
      </g>
    </g>

    <!-- bullet rails -->
    <g stroke="var(--gold-line)" stroke-width="1" fill="none">
      <path d="M107 407 V489"/>
      <path d="M400 407 V485 M400 493 V557"/>
      <path d="M840 407 V522"/>
      <path d="M990 397 V431 M990 439 V494"/>
    </g>
    <g fill="#fff" stroke="var(--gold-line)" stroke-width="1.1">
      <path d="M107 399 L111 403 L107 407 L103 403 Z"/>
      <path d="M107 489 L111 493 L107 497 L103 493 Z"/>
      <path d="M255 399 L259 403 L255 407 L251 403 Z"/>
      <path d="M400 399 L404 403 L400 407 L396 403 Z"/>
      <path d="M400 485 L404 489 L400 493 L396 489 Z"/>
      <path d="M400 557 L404 561 L400 565 L396 561 Z"/>
      <path d="M545 399 L549 403 L545 407 L541 403 Z"/>
      <path d="M691 399 L695 403 L691 407 L687 403 Z"/>
      <path d="M840 399 L844 403 L840 407 L836 403 Z"/>
      <path d="M840 522 L844 526 L840 530 L836 526 Z"/>
      <path d="M990 389 L994 393 L990 397 L986 393 Z"/>
      <path d="M990 431 L994 435 L990 439 L986 435 Z"/>
      <path d="M990 494 L994 498 L990 502 L986 498 Z"/>
    </g>

    <!-- next-step buttons -->
    <g fill="none" stroke="#d4bb8c" stroke-width="1.5" stroke-linecap="round">
      <circle cx="160" cy="625" r="22" fill="var(--blush)" stroke="none"/><path d="M152 625 H167 M162 620 L167 625 L162 630"/>
      <circle cx="310" cy="625" r="22" fill="var(--blush)" stroke="none"/><path d="M302 625 H317 M312 620 L317 625 L312 630"/>
      <circle cx="451" cy="625" r="22" fill="var(--blush)" stroke="none"/><path d="M443 625 H458 M453 620 L458 625 L453 630"/>
      <circle cx="602" cy="625" r="22" fill="var(--blush)" stroke="none"/><path d="M594 625 H609 M604 620 L609 625 L604 630"/>
      <circle cx="747" cy="625" r="22" fill="var(--blush)" stroke="none"/><path d="M739 625 H754 M749 620 L754 625 L749 630"/>
      <circle cx="895" cy="625" r="22" fill="var(--blush)" stroke="none"/><path d="M887 625 H902 M897 620 L902 625 L897 630"/>
    </g>
  </svg>

  <!-- step names -->
  <div class="step-name" style="left:92px">Listening</div>
  <div class="step-name" style="left:238px">Visioning</div>
  <div class="step-name" style="left:384px">Planning</div>
  <div class="step-name" style="left:530px">Designing</div>
  <div class="step-name" style="left:676px">Managing</div>
  <div class="step-name" style="left:822px">Installing</div>
  <div class="step-name" style="left:968px">Completing</div>

  <!-- step notes -->
  <p class="step-note" style="left:123px;top:380px;width:92px">Listening to our clients, their land, and their home</p>
  <p class="step-note" style="left:123px;top:468px;width:92px">Identifying their needs, challenges, wishes, and dreams</p>

  <p class="step-note" style="left:269px;top:380px;width:98px">Facilitating a guided visioning process to clarify the deepest intention, true purposes, and highest potential for their home and their future within it</p>

  <p class="step-note" style="left:412px;top:380px;width:100px">Turning our client's vision into a clearly defined scope, budget, and timeline.</p>
  <p class="step-note" style="left:412px;top:470px;width:92px">Mapping out the steps for making thier dream a reality.</p>
  <p class="step-note" style="left:412px;top:543px;width:100px">Setting a meeting schedule from start to finish.</p>

  <p class="step-note" style="left:554px;top:380px;width:112px">Following the schedule through the design phases from initial design concepts, technical drawings and details, and the selection of all finishes, fixtures, and surnishings.</p>

  <p class="step-note" style="left:699px;top:380px;width:112px">Cordinating with clients, builders, architects, and vendors to ensure that the design is executed with excellence, and the construction and furnishings are on-time and on-budget.</p>

  <p class="step-note" style="left:851px;top:380px;width:108px">Overseeing the inspection, installation, and arrangement of all furnishings, lighting, artwork, and decorative items.</p>
  <p class="step-note" style="left:851px;top:512px;width:90px">Taking care of every last detail.</p>

  <p class="step-note" style="left:999px;top:380px;width:102px">Fixing any issues or defects.</p>
  <p class="step-note" style="left:999px;top:425px;width:102px">Follow up on all remaining items.</p>
  <p class="step-note" style="left:999px;top:469px;width:100px">Completing the final finishing touches to our client's full and total satisfaction.</p>

  <!-- testimonials -->
  <h2 class="testimonials-title">Testimonials</h2>

  <div class="quote-num" style="left:81px">1.</div>
  <p class="quote" style="left:152px">Dana to send over testimonials for fill this space - three or four columns of testimonials</p>
  <div class="quote-num" style="left:345px">2.</div>
  <p class="quote" style="left:415px">Dana to send over testimonials for fill this space - three or four columns of testimonials</p>
  <div class="quote-num" style="left:608px">3.</div>
  <p class="quote" style="left:678px">Dana to send over testimonials for fill this space - three or four columns of testimonials</p>
  <div class="quote-num" style="left:870px">4.</div>
  <p class="quote" style="left:940px">Dana to send over testimonials for fill this space - three or four columns of testimonials</p>

</div>
</body>
</html>
```